new KVR one page flyer

We need a 1 page A4 size flyer (need it asap please) that describes on 1 page with art work and using photos the services we provide. I have included some examples of old previous flyers from our other (seperate divisions of the business) I have named a photo called (photo for top of design) however you do your design this photo needs to be the star of the page by either having it at the top or bottom of the page please and we usually like this photo to be in greyscale colour.
we do like greyscale designs but are open to see what you come up with as a whole page of grey white and black might not suit.

Needs to list the following

Services include:
Over size loads / Hot Shot Loads
Heavy Vehicle Recovery services
Potable Water Deliveries
Road Building / Maintenance
Earthworks
Sand & Metal Supply & Cartage
Road Train Tippers
Road Train Tankers
Road Train Flat Tops
Drop Deck Trailers
Mine site accredited equipment & Operators.

We offer a large rage of services not listed so call us today for a personalised quote to suit your needs.

To go on the bottom of the page our contact details are

KVR Pty Ltd
Depot: Lot 514, Banksia Flats Track Gidgee Springs
Mobile: 047 216 9381
email: darren@kestrelvaleroadworks.com.au

Target Market(s)

new clients

Colors

Designer to choose colors to be used in the design.

Requirements
Must have
• our services listed
Nice to have
• stand out designs

```html
<!DOCTYPE html>
<html lang="en">
<head>
<meta charset="utf-8">
<title>KVR Pty Ltd – Services Flyer</title>
<link href="https://fonts.googleapis.com/css2?family=Arimo:wght@400;700&family=Roboto+Condensed:wght@400;700&display=swap" rel="stylesheet">
<style>
  :root{
    --bg-light:#5c5c5e;
    --bg-dark:#262627;
    --cream:#ece7da;
    --text-light:#e2ded5;
    --tick:#b9b7b2;
    --panel:#6c6c6f;
    --panel-text:#ececec;
    --title:#3b3b3d;
    --badge:#1c1c1e;
  }
  *{margin:0;padding:0;box-sizing:border-box}
  html,body{width:848px;height:1200px;overflow:hidden;background:#fff}
  .flyer{
    position:relative;width:848px;height:1200px;overflow:hidden;
    background:linear-gradient(160deg,var(--bg-light) 0%,#3f3f41 45%,var(--bg-dark) 100%);
    font-family:"Arimo",Arial,sans-serif;
  }
  .hero{position:absolute;left:0;top:0;width:848px;height:470px}
  .company-title{
    position:absolute;left:288px;top:121px;line-height:1;
    font-size:56px;font-weight:400;color:var(--title);letter-spacing:2.7px;white-space:nowrap;
  }
  .headline{
    position:absolute;left:84px;top:477px;
    font-size:66px;line-height:62px;font-weight:400;color:var(--cream);white-space:nowrap;
  }
  .services{
    position:absolute;left:100px;top:617px;list-style:none;
  }
  .services li{
    display:flex;align-items:center;height:26.7px;
    font-size:21px;color:var(--text-light);white-space:nowrap;
  }
  .services svg{width:16px;height:14px;margin-right:10px;flex:none}
  .badge{
    position:absolute;left:558px;top:674px;width:133px;height:146px;
    border-radius:12px;background:var(--badge);
    display:flex;align-items:center;justify-content:center;
    font-size:40px;font-weight:700;color:#cfcfd2;letter-spacing:2px;
  }
  .quote-panel{
    position:absolute;left:53px;top:930px;width:742px;height:82px;
    border-radius:6px;background:var(--panel);
    padding:8px 10px 0 21px;
    font-family:"Roboto Condensed","Arial Narrow",sans-serif;
    font-weight:700;font-size:19px;line-height:34px;letter-spacing:1.2px;color:var(--panel-text);
    text-transform:uppercase;white-space:nowrap;
  }
  .contact{position:absolute;left:101px;white-space:nowrap;color:var(--text-light)}
  .contact.mobile{top:1029px;font-family:"Roboto Condensed","Arial Narrow",sans-serif;font-size:27px}
  .contact.depot{top:1072px;font-family:"Arimo",Arial,sans-serif;font-size:27px}
  .contact.email{top:1116px;display:flex;align-items:center;font-family:"Arimo",Arial,sans-serif;font-size:27.5px}
  .contact.email svg{width:31px;height:20px;margin-right:25px}
</style>
</head>
<body>
<div class="flyer">
  <svg class="hero" viewBox="0 0 848 470" role="img" aria-label="Greyscale photo of a road train tipper truck on an outback road under a cloudy sky">
    <defs>
      <linearGradient id="heroTone" x1="0" y1="0" x2="0" y2="1">
        <stop offset="0" stop-color="#8f9399"/>
        <stop offset=".45" stop-color="#b9bbbd"/>
        <stop offset=".62" stop-color="#6e6a64"/>
        <stop offset=".8" stop-color="#a59e95"/>
        <stop offset="1" stop-color="#e8e6e3"/>
      </linearGradient>
    </defs>
    <polygon fill="url(#heroTone)" points="0,0 848,0 848,300 800,350 752,400 704,440 660,400 616,360 572,400 528,440 480,380 432,420 380,360 328,410 280,470 232,420 184,370 128,420 80,380 40,340 0,310"/>
    <g fill="none" stroke="#ffffff" stroke-opacity=".35" stroke-width="2">
      <polygon points="420,180 520,280 420,380 320,280"/>
      <polygon points="720,150 840,270 720,390 600,270"/>
      <polygon points="140,220 230,310 140,400 50,310"/>
    </g>
    <g fill="#3a3a3c">
      <polygon points="240,0 300,60 360,0"/>
      <polygon points="470,0 540,70 610,0"/>
      <polygon points="0,120 30,150 0,180"/>
    </g>
  </svg>
  <div class="company-title">KVR Pty Ltd</div>

  <h1 class="headline">WE PROVIDE<br>THE BEST SERVICES</h1>

  <ul class="services">
    <li><svg viewBox="0 0 16 14"><path d="M1 8 L6 12 L15 2" fill="none" stroke="var(--tick)" stroke-width="2.4"/></svg>Over size loads / Hot Shot Loads</li>
    <li><svg viewBox="0 0 16 14"><path d="M1 8 L6 12 L15 2" fill="none" stroke="var(--tick)" stroke-width="2.4"/></svg>Heavy Vehicle Recovery services</li>
    <li><svg viewBox="0 0 16 14"><path d="M1 8 L6 12 L15 2" fill="none" stroke="var(--tick)" stroke-width="2.4"/></svg>Potable Water Deliveries</li>
    <li><svg viewBox="0 0 16 14"><path d="M1 8 L6 12 L15 2" fill="none" stroke="var(--tick)" stroke-width="2.4"/></svg>Road Building / Maintenance</li>
    <li><svg viewBox="0 0 16 14"><path d="M1 8 L6 12 L15 2" fill="none" stroke="var(--tick)" stroke-width="2.4"/></svg>Earthworks</li>
    <li><svg viewBox="0 0 16 14"><path d="M1 8 L6 12 L15 2" fill="none" stroke="var(--tick)" stroke-width="2.4"/></svg>Sand &amp; Metal Supply &amp; Cartage</li>
    <li><svg viewBox="0 0 16 14"><path d="M1 8 L6 12 L15 2" fill="none" stroke="var(--tick)" stroke-width="2.4"/></svg>Road Train Tippers</li>
    <li><svg viewBox="0 0 16 14"><path d="M1 8 L6 12 L15 2" fill="none" stroke="var(--tick)" stroke-width="2.4"/></svg>Road Train Tankers</li>
    <li><svg viewBox="0 0 16 14"><path d="M1 8 L6 12 L15 2" fill="none" stroke="var(--tick)" stroke-width="2.4"/></svg>Road Train Flat Tops</li>
    <li><svg viewBox="0 0 16 14"><path d="M1 8 L6 12 L15 2" fill="none" stroke="var(--tick)" stroke-width="2.4"/></svg>Drop Deck Trailers</li>
    <li><svg viewBox="0 0 16 14"><path d="M1 8 L6 12 L15 2" fill="none" stroke="var(--tick)" stroke-width="2.4"/></svg>Mine site accredited equipment &amp; Operators</li>
  </ul>

  <div class="badge">KVR</div>

  <p class="quote-panel">We offer a large range of services not listed so call us today for a<br>personalised quote to suit your needs.</p>

  <p class="contact mobile">Mobile: 047 216 9381</p>
  <p class="contact depot">Depot: Lot 514, Banksia Flats Track Gidgee Springs</p>
  <p class="contact email"><svg viewBox="0 0 30 20"><rect x="1" y="1" width="28" height="18" fill="none" stroke="var(--text-light)" stroke-width="2"/><path d="M1 1 L15 12 L29 1" fill="none" stroke="var(--text-light)" stroke-width="2"/></svg>darren@kestrelvaleroadworks.com.au</p>
</div>
</body>
</html>
```